I would like a color, double sided, gate folded brochure based off of 8.5"x11" paper.I have attached a word file with information that I would like contained within the brochure. The logo that I was told to use for this brochure is attached, but it is of low quality. Please do with it what you can, and we would prefer the color blue instead of purple, if at all possible. The logo would go on the front of the brochure, along with the text"Benton Valley Helping Circle" & "Always Beside You...", just without the quotes.The only other item that we would like in a certain spot, is a card that could be cut out of the back side of the brochure and mailed in with a donation. On it, we would like lines for someone to write their Name, Address, City, State, Zip Code, Phone, E-mail Address. AT the bottom of the card, we would like it to say "Please mail card and donation payable to Benton Valley Helping Circle, PO Box 587, Millbrook, OH 44698".Our facebook page is called Benton Valley Helping Circle (https://www.example-social.com/Benton-Valley-Helping-Circle-513904267185649/), and you can find various photos there to use on the brochure. There are pictures from a bingo contest, outdoor cookout, and bake sale, and would like a picture (or more) used from each within the brochure.

Colors

Designer to choose colors to be used in the design.

Requirements
Must have
• I need a brochure that uses a gate fold.

```html
<!DOCTYPE html>
<html lang="en">
<head>
<meta charset="utf-8">
<title>Benton Valley Helping Circle – Gate Fold Brochure</title>
<link href="https://fonts.googleapis.com/css2?family=Encode+Sans+Condensed:wght@400;600;700&family=Ubuntu:wght@400;500;700&family=Ubuntu+Mono:ital@1&family=Open+Sans:ital,wght@0,400;0,700;1,400&display=swap" rel="stylesheet">
<style>
:root{
  --navy:#13295a;
  --deep:#1b4f96;
  --blue:#2677c6;
  --cyan:#25b4e8;
  --sky:#a9dcf3;
  --ink:#1d2f5e;
  --paper:#ffffff;
  --bg:#e9eaec;
}
*{box-sizing:border-box;margin:0;padding:0}
html,body{width:1200px;height:900px;overflow:hidden;background:var(--bg)}
body{position:relative;font-family:"Encode Sans Condensed",sans-serif;color:var(--ink)}
.spread{position:absolute;overflow:hidden;box-shadow:0 4px 10px rgba(0,0,0,.25)}
.spread--outside{left:58px;top:32px;width:542px;height:418px}
.spread--inside{left:599px;top:450px;width:543px;height:420px;background:linear-gradient(180deg,#fff 0%,#fff 45%,#cfcfd1 100%)}
.panel{position:absolute;top:0;height:100%;overflow:hidden}
.panel--left-flap{left:0;width:138px;background:var(--paper)}
.panel--back{left:138px;width:267px;background:linear-gradient(180deg,#fff 30%,#b9b9bb 100%)}
.panel--right-flap{left:405px;width:137px;background:var(--paper)}
.wave{position:absolute;left:0;width:100%}
.cover-square{position:absolute;width:58px;height:114px;background:linear-gradient(180deg,var(--blue),var(--cyan))}
.cover-name{position:absolute;top:242px;font-family:Ubuntu,sans-serif;font-weight:500;font-size:13px;color:var(--cyan);white-space:nowrap;letter-spacing:.4px}
.slogan{font-family:"Ubuntu Mono",monospace;font-style:italic;letter-spacing:2px;color:var(--cyan)}
.flap-slogan{position:absolute;top:382px;font-size:15px;white-space:nowrap}
.masthead{position:absolute;left:17px;top:10px;display:flex;align-items:center;gap:7px}
.masthead__square{width:14px;height:14px;background:#fff}
.masthead__name{font-family:Ubuntu,sans-serif;font-weight:500;font-size:12px;line-height:19px;color:#fff;letter-spacing:.5px}
.back-copy{position:absolute;left:14px;right:10px;text-align:center;font-size:8px;line-height:10.5px}
.board{top:134px;left:44px;right:32px;font-style:italic;font-weight:600;font-size:8px}
.board b{font-style:normal;font-weight:400;font-size:10.5px;letter-spacing:.3px}
.help-title{top:185px;font-size:11px;letter-spacing:.4px}
.contact{top:203px;line-height:13.5px;font-size:7px}
.contact strong{font-weight:600;font-size:8px}
.contact em{font-weight:600;font-size:8px}
.card-note{top:303px;font-size:6.5px;line-height:8.5px;font-style:italic;font-weight:600}
.scissors{position:absolute;left:70px;top:324px}
.donation-card{position:absolute;left:57px;top:340px;width:154px;height:90px;border:1px dashed #555;padding:8px 12px 0}
.card-line{display:flex;align-items:flex-end;height:14px;font-size:4.5px;font-weight:700;border-bottom:.6px solid #555}
.card-line--split{display:flex;gap:6px;border:none}
.card-line--split span{flex:1;border-bottom:.6px solid #555;height:14px;display:flex;align-items:flex-end}
.inside-title{position:absolute;left:79px;top:16px;font-family:"Open Sans",sans-serif;font-style:italic;font-weight:400;font-size:14px;line-height:23px;letter-spacing:1.2px;color:var(--cyan);text-transform:uppercase}
.photo{position:absolute;border:2px solid #fff;box-shadow:0 1px 4px rgba(0,0,0,.45)}
.photo--volunteers{left:266px;top:76px;width:97px;height:67px;background:linear-gradient(160deg,#8a6a4c,#cfc9bd 60%,#4c5d7a)}
.photo--cookout{left:410px;top:76px;width:98px;height:67px;background:linear-gradient(170deg,#c9d2d9,#6e6b66 55%,#3b3a38)}
.photo--bingo{left:72px;top:155px;width:97px;height:65px;background:linear-gradient(180deg,#d8d9dc,#8e8270 55%,#7a3a30)}
.photo--bakesale{left:197px;top:155px;width:96px;height:65px;background:linear-gradient(170deg,#6b4a2f,#c9a28a 45%,#b84a1e)}
.photo--family{left:371px;top:243px;width:98px;height:75px;background:linear-gradient(170deg,#9ab0a0,#494a4c 50%,#a5282b)}
.q{position:absolute;font-family:"Open Sans",sans-serif;font-size:7.3px;line-height:9.6px;color:var(--navy)}
.q b{font-family:Ubuntu,sans-serif;font-weight:700;font-size:10px;letter-spacing:.4px}
.q--who{left:67px;top:84px;width:176px}
.q--purpose{left:326px;top:171px;width:186px}
.q--funds{left:81px;top:237px;width:250px}
.q--apply{left:97px;top:300px;width:262px}
.footer-mark{position:absolute;left:170px;top:360px;display:flex;align-items:center;gap:6px}
.footer-mark__square{width:12px;height:12px;background:var(--blue)}
.footer-mark__name{font-family:Ubuntu,sans-serif;font-weight:500;font-size:8px;line-height:10px;color:var(--deep)}
.footer-slogan{position:absolute;left:271px;top:356px;font-size:15px;line-height:18px;color:var(--deep)}
</style>
</head>
<body>

<section class="spread spread--outside" aria-label="Outside of brochure">
  <div class="panel panel--left-flap">
    <svg class="wave" style="top:0;height:80px" viewBox="0 0 138 80" preserveAspectRatio="none">
      <path d="M0 0H30C22 20 10 40 0 50Z" fill="var(--blue)"/>
      <path d="M30 0H90C60 20 30 45 0 62V50C10 40 22 20 30 0Z" fill="var(--sky)" opacity=".6"/>
    </svg>
    <div class="cover-square" style="left:0;top:108px"></div>
    <div class="cover-name" style="right:-6px">Helping Circle</div>
    <svg class="wave" style="top:260px;height:158px" viewBox="0 0 138 158" preserveAspectRatio="none">
      <path d="M0 80C50 60 100 40 138 30V158H0Z" fill="var(--cyan)"/>
      <path d="M0 92C50 70 100 56 138 50V158H0Z" fill="var(--blue)"/>
      <path d="M0 100C50 84 100 74 138 70V158H0Z" fill="var(--navy)"/>
    </svg>
    <div class="slogan flap-slogan" style="left:9px">Beside You</div>
  </div>

  <div class="panel panel--back">
    <svg class="wave" style="top:0;height:124px" viewBox="0 0 267 124" preserveAspectRatio="none">
      <path d="M0 0H267C220 40 120 95 0 124Z" fill="var(--sky)"/>
      <path d="M0 0H240C200 40 110 80 0 100Z" fill="var(--cyan)"/>
      <path d="M0 0H200C150 30 80 60 0 78Z" fill="var(--blue)"/>
    </svg>
    <div class="masthead">
      <div class="masthead__square"></div>
      <div class="masthead__name">Benton Valley<br>Helping Circle</div>
    </div>
    <p class="back-copy board"><b>BOARD MEMBERS:</b> Marian Holt, Kelly Ashford, Dana Whitcomb, Clara Renshaw, Tina Marlowe, Dee Parrish, Alice Brennan, and Bev Hollis.</p>
    <p class="back-copy help-title">HOW CAN I HELP OR VOLUNTEER AT FUNRAISERS?</p>
    <p class="back-copy contact">
      Contact <strong>Marian Holt</strong> at <em>330-555-0142</em><br>
      or <strong>Clara Renshaw</strong> at <em>330-555-0187.</em><br>
      You may also send an email<br>
      to <em>bvhc4u@example.com</em><br>
      or write to us at<br>
      <em>Benton Valley Helping Circle, PO Box 587,</em><br>
      <em>Millbrook, OH 44698</em>
    </p>
    <p class="back-copy card-note">Please mail card and donation payable<br>to Benton Valley Helping Circle</p>
    <svg class="scissors" width="34" height="18" viewBox="0 0 34 18" aria-hidden="true">
      <circle cx="4" cy="5" r="3" fill="none" stroke="#222" stroke-width="1.2"/>
      <circle cx="4" cy="14" r="3" fill="none" stroke="#222" stroke-width="1.2"/>
      <path d="M6.5 6.5L32 13M6.5 12.5L30 2" stroke="#222" stroke-width="1.2"/>
    </svg>
    <div class="donation-card">
      <div class="card-line">Name:</div>
      <div class="card-line">Address:</div>
      <div class="card-line">City/State/Zip Code:</div>
      <div class="card-line card-line--split"><span>Phone:</span><span>Mail:</span></div>
    </div>
  </div>

  <div class="panel panel--right-flap">
    <svg class="wave" style="top:0;height:80px" viewBox="0 0 137 80" preserveAspectRatio="none">
      <path d="M0 0H137V25C90 50 40 62 0 60Z" fill="var(--cyan)"/>
      <path d="M137 25C90 50 40 62 0 60V62C40 66 100 58 137 40Z" fill="var(--sky)"/>
    </svg>
    <div class="cover-square" style="left:81px;top:108px"></div>
    <div class="cover-name" style="left:50px">Benton Valley</div>
    <svg class="wave" style="top:320px;height:98px" viewBox="0 0 137 98" preserveAspectRatio="none">
      <path d="M0 0C50 8 100 8 137 2V98H0Z" fill="var(--blue)"/>
      <path d="M0 6C50 14 100 14 137 10V98H0Z" fill="var(--navy)"/>
    </svg>
    <div class="slogan flap-slogan" style="left:75px">Always</div>
  </div>
</section>

<section class="spread spread--inside" aria-label="Inside of brochure">
  <svg class="wave" style="top:0;height:420px;width:543px" viewBox="0 0 543 420" preserveAspectRatio="none">
    <path d="M0 0H70C30 80 20 220 137 420H0Z" fill="var(--navy)"/>
    <path d="M70 0C30 80 20 220 137 420H100C10 260 20 100 55 0Z" fill="var(--deep)"/>
    <path d="M45 0C15 110 15 260 100 420H70C5 280 5 120 30 0Z" fill="var(--cyan)"/>
    <path d="M543 160C500 260 460 360 380 420H543Z" fill="var(--sky)"/>
    <path d="M543 200C510 290 480 370 420 420H543Z" fill="var(--cyan)"/>
    <path d="M543 220C520 300 500 370 455 420H543Z" fill="var(--blue)"/>
  </svg>
  <h1 class="inside-title">A new 501(c)3 non-profit group for helping families<br>with medical or catastrophic events .</h1>

  <p class="q q--who"><b>WHO ARE WE:</b> A group of experienced fundraisers who wish to assist Benton Valley residents with medical needs. We formed Benton Valley Helping Circle to provide a service to the county.</p>
  <div class="photo photo--volunteers" role="img" aria-label="Photo of two volunteers in a kitchen"></div>
  <div class="photo photo--cookout" role="img" aria-label="Photo of the outdoor cookout under a tent"></div>
  <div class="photo photo--bingo" role="img" aria-label="Photo of a crowded bingo night in a hall"></div>
  <div class="photo photo--bakesale" role="img" aria-label="Photo of baskets at the bake sale table"></div>
  <p class="q q--purpose"><b>WHAT IS OUR PURPOSE:</b> To provide short-term charitable assistance to Benton Valley residents with out-of-pocket expenses incurred due to illness or catastrophic events.</p>
  <p class="q q--funds"><b>WHERE DO OUR FUNDS COME FROM?</b> The organization conducts fundraisers and accepts donations. We are 501(c)3 tax exempt, so all donations are tax deductible. We are also planning to apply for any applicable grants that might be available. All donations are appreciated.</p>
  <div class="photo photo--family" role="img" aria-label="Photo of a family at an outdoor event"></div>
  <p class="q q--apply"><b>HOW DO PEOPLE APPLY FOR ASSISTANCE:</b> Applications are available at Valley General Hospital from Nora Hale and at the Community Hall at the Fairgrounds. Residents can also contact any member of the board to give information and help to someone in need.</p>

  <div class="footer-mark">
    <div class="footer-mark__square"></div>
    <div class="footer-mark__name">Benton Valley<br>Helping Circle</div>
  </div>
  <div class="slogan footer-slogan">Always<br>Beside You</div>
</section>

</body>
</html>
```